LUPO Baby Massage Classes - flyer to make a difference

I need a single page flyer, preferably single page, to hand out to doctors, medical centres and parents. To also leave on counters of establishments.
It is to promote my baby massage classes. Mums can get together with other mums and book a 5 week course to learn and discover the many benefits of baby massage.
Benefits include: enhances bonding and attachment, understand non-verbal cues from your baby, helps with sleep patterns, help with immune system, increases vagal activity,relief from wind, colic or constipation to name some.

Baby age from birth to 12 months. Group classes or private sessions

I am a Professional Member and Certified by the Global Guild of Cradle Touch (GGCT) GGCT Australia is Nationally Accredited and is endorsed by Crestfield Board of Carers, the Southvale Council of Birthworkers, The Westbrook Society of Daily Living Practice Oceania, The Harbourline Union of Bodywork Practitioner and is a full member of Kindred Wellbeing Network.

Class detail and availability contact is Carol Perkins 0478 315 027 carol.jean.perkins@examplemail.net www.lupocradletouch com.au facebook/comLUPOcradletouch

My colour scheme is green and purple as you will see from my logo and website. I would like my flyer to be softer tones of either both colours or just one.

I will include some images you can choose from or show me any you think will fit in with baby massage. THANK YOU
Updates

Hi The size of my flyer is A6. Approx 150mms x 210mms and single sided. Thank you

Target Market(s)

mums and dads, groups, doctors, midwives

Industry/Entity Type

Medical

Font styles to use
Sans Serif

Colors
87d0c7
b09cc8

Requirements
Must have
• baby photo or photos, both my logo and the GGCT logo. The GGCT logo is to be small
• Baby Massage Classes (wording) is very important to catch the eye.
• Invitation to book a class or gather friends to book is next in importance
• Benefits is next
• The admin information ie.,membership, certification and endorsements are lesser and can be small.
• Contact information to be noticeable.
Nice to have
• If you have an idea, drawing or photo that would look better, please feel free to try it
Should not have
• should not be crowded with information all the same size

```html
<!DOCTYPE html>
<html lang="en">
<head>
<meta charset="utf-8">
<title>LUPO Baby Massage Classes flyer</title>
<link rel="stylesheet" href="https://fonts.googleapis.com/css2?family=Arimo:ital,wght@0,400;0,700;1,700&family=Roboto+Condensed:ital,wght@0,400;1,700&display=swap">
<style>
  :root {
    --purple: #8e2a8c;
    --teal: #14a89c;
    --teal-soft: #2bb3a6;
    --ink: #111111;
    --white: #ffffff;
    --canvas: #ffffff;
  }
  * { margin: 0; padding: 0; box-sizing: border-box; }
  html, body { width: 1200px; height: 1000px; overflow: hidden; background: var(--canvas); }
  .canvas { position: relative; width: 1200px; height: 1000px; }
  .flyer {
    position: absolute; left: 250px; top: 10px; width: 700px; height: 980px;
    background: var(--white); overflow: hidden;
    box-shadow: 4px 6px 14px rgba(0,0,0,0.35);
    font-family: "Arimo", Arial, sans-serif;
  }
  .flyer-shapes { position: absolute; left: 0; top: 0; }
  .abs { position: absolute; }
  .brand { left: 50px; top: 115px; display: flex; align-items: center; gap: 12px; }
  .brand-dot { width: 100px; height: 100px; border-radius: 50%; background: var(--teal-soft); }
  .brand-name { font-family: "Arimo", Arial, sans-serif; font-weight: 700; font-size: 42px; color: var(--teal-soft); letter-spacing: 1px; }
  .age-badge {
    left: 118px; top: 281px; width: 164px; height: 164px; border-radius: 50%;
    background: var(--purple); color: var(--white);
    font-family: "Roboto Condensed", "Arial Narrow", sans-serif; font-size: 25px; line-height: 36px;
    padding: 30px 0 0 22px; white-space: nowrap;
  }
  .benefits-title, .about-title {
    color: var(--purple); font-weight: 700; font-style: italic; font-size: 20px; letter-spacing: 2px;
  }
  .benefits-title { left: 31px; top: 446px; }
  .benefits-list { left: 35px; top: 475px; list-style: none; font-size: 20px; line-height: 27px; color: var(--ink); letter-spacing: 1.3px; white-space: nowrap; }
  .benefits-list .wrap { padding-left: 41px; }
  .about-title { left: 10px; top: 692px; }
  .about-text {
    left: 10px; top: 725px; width: 360px; color: var(--white);
    font-family: "Roboto Condensed", "Arial Narrow", sans-serif; font-size: 15.5px; line-height: 23px;
  }
  .enquire {
    left: 372px; top: 668px; width: 122px; height: 97px; border-radius: 10px;
    background: var(--purple); color: var(--white);
    font-family: "Roboto Condensed", "Arial Narrow", sans-serif; font-style: italic; font-weight: 700;
    font-size: 15px; line-height: 29px; padding: 4px 0 0 10px; white-space: nowrap;
  }
  .sessions {
    left: 392px; top: 752px; width: 196px; height: 196px; border-radius: 50%;
    background: var(--purple); color: var(--white); text-align: center;
    font-family: "Roboto Condensed", "Arial Narrow", sans-serif; font-size: 24px; line-height: 36px;
    padding-top: 45px; white-space: nowrap;
  }
  .contact {
    left: 473px; top: 605px; width: 210px; height: 210px; border-radius: 50%;
    background: var(--teal); color: var(--white); border: 4px solid var(--white);
    font-family: "Roboto Condensed", "Arial Narrow", sans-serif;
    display: flex; flex-direction: column; align-items: center; justify-content: center;
    white-space: nowrap; gap: 6px; padding-bottom: 6px;
  }
  .contact-name { font-size: 33px; line-height: 46px; }
  .contact-phone { font-size: 35px; line-height: 46px; letter-spacing: -0.3px; }
  .accreditation-badge {
    left: 580px; top: 820px; width: 110px; height: 74px; border-radius: 8px; background: var(--teal-soft);
  }
  .footer {
    left: 0; top: 918px; width: 700px; height: 41px; background: var(--purple); color: var(--white);
    font-family: "Roboto Condensed", "Arial Narrow", sans-serif; font-style: italic; font-weight: 700; font-size: 16px;
    display: flex; justify-content: space-between; align-items: center; padding: 0 8px 0 20px; white-space: nowrap;
  }
  .footer-base { left: 0; top: 959px; width: 700px; height: 21px; background: var(--teal); }
</style>
</head>
<body>
<div class="canvas">
  <div class="flyer">
    <svg class="flyer-shapes" width="700" height="980" viewBox="0 0 700 980">
      <defs>
        <linearGradient id="photoTone" x1="0" y1="0" x2="1" y2="1">
          <stop offset="0" stop-color="#f1f2f6"/>
          <stop offset="0.55" stop-color="#e6d6cb"/>
          <stop offset="1" stop-color="#c9a792"/>
        </linearGradient>
      </defs>
      <path class="photo-area" role="img" aria-label="Photo of a smiling baby lying on a white blanket while a parent's hands massage its tummy"
            d="M290 0 L700 0 L700 505 C600 480 450 420 265 410 C285 300 310 180 290 0 Z" fill="url(#photoTone)"/>
      <path d="M280 0 C320 120 320 220 250 305" fill="none" stroke="var(--purple)" stroke-width="6"/>
      <path d="M40 180 C50 240 110 255 170 245" fill="none" stroke="var(--purple)" stroke-width="12" stroke-linecap="round"/>
      <path d="M240 410 C420 430 560 500 640 640" fill="none" stroke="var(--purple)" stroke-width="7"/>
      <path d="M0 590 C60 640 200 690 380 700 L380 918 L0 918 Z" fill="var(--teal)"/>
      <path d="M330 705 C400 690 470 700 560 690" fill="none" stroke="var(--teal)" stroke-width="10"/>
    </svg>

    <div class="abs brand"><span class="brand-dot"></span><span class="brand-name">LUPO</span></div>

    <div class="abs age-badge">Baby age<br>from birth to<br>12 months</div>

    <h2 class="abs benefits-title">Baby massage benefits:</h2>
    <ul class="abs benefits-list">
      <li>Enhances bonding and attachment</li>
      <li>Understand non-verbal cues from your baby</li>
      <li>Helps with sleep patterns</li>
      <li>Help with immune system</li>
      <li>Increases vagal activity</li>
      <li>Relief from wind, colic or constipation to name</li>
      <li class="wrap">some.</li>
    </ul>

    <h2 class="abs about-title">About me:</h2>
    <p class="abs about-text">I am a Professional Member and Certified by the Global Guild of Cradle Touch (GGCT) GGCT Australia is Nationally Accredited and is endorsed by Crestfield Board of Carers, the Southvale Council of Birthworkers, The Westbrook Society of Daily Living Practice Oceania, The Harbourline Union of Bodywork Practitioner and is a full member of Kindred Wellbeing Network.</p>

    <div class="abs enquire">For Class detail<br>and availability<br>contact:</div>
    <div class="abs sessions">Group classes<br>or<br>private sessions</div>
    <div class="abs contact">
      <span class="contact-name">Carol Perkins</span>
      <span class="contact-phone">0478 315 027</span>
    </div>
    <div class="abs accreditation-badge" role="img" aria-label="Accreditation badge"></div>

    <div class="abs footer">
      <span>carol.jean.perkins@examplemail.net www.lupocradletouch com.au</span>
      <span>facebook/comLUPOcradletouch</span>
    </div>
    <div class="abs footer-base"></div>
  </div>
</div>
</body>
</html>
```